Surveillance Sign

Design sign and stickers with a line drawing of the camera.

Industry/Entity Type

Camera

Requirements
Nice to have
• I like this design: http://www.varnotek.com/cctv-camera-warning-signs-decals/camera-surveillance-sign

```html
<!DOCTYPE html>
<html lang="en">
<head>
<meta charset="utf-8">
<title>Surveillance Sign</title>
<link rel="stylesheet" href="https://fonts.googleapis.com/css2?family=Roboto:wght@700;900&display=swap">
<style>
  :root {
    --sign-red: #ec1c24;
    --warning-yellow: #ffe512;
    --ink: #111111;
    --paper: #ffffff;
    --illustration-light: #eeeeee;
    --illustration-dark: #9a9a9a;
  }
  * { margin: 0; padding: 0; box-sizing: border-box; }
  html, body {
    width: 1200px;
    height: 921px;
    overflow: hidden;
    background: var(--paper);
  }
  .canvas {
    position: relative;
    width: 1200px;
    height: 921px;
    background: var(--paper);
    font-family: "Roboto", Arial, sans-serif;
  }
  .sign {
    position: absolute;
    left: 60px;
    top: 52px;
    width: 1078px;
    height: 813px;
    background: var(--sign-red);
    border: 4px solid var(--ink);
    border-radius: 34px;
    overflow: hidden;
  }
  .title-plate {
    position: absolute;
    left: 76px;
    top: 29px;
    width: 916px;
    height: 140px;
    background: var(--warning-yellow);
    border: 5px solid var(--ink);
    border-radius: 16px;
    display: flex;
    align-items: center;
    justify-content: center;
  }
  .title-plate h1 {
    font-weight: 900;
    font-size: 116px;
    line-height: 1;
    color: var(--ink);
    letter-spacing: 1px;
  }
  .notice-band {
    position: absolute;
    left: 0;
    top: 197px;
    width: 100%;
    height: 408px;
    background: var(--paper);
  }
  .camera-illustration {
    position: absolute;
    left: 26px;
    top: 24px;
    width: 580px;
    height: 362px;
    border-radius: 8px;
    background: linear-gradient(135deg, var(--illustration-light), var(--illustration-dark));
  }
  .notice-text {
    position: absolute;
    left: 615px;
    top: 22px;
    width: 400px;
    text-align: center;
    font-weight: 900;
    font-size: 56px;
    line-height: 62px;
    color: var(--ink);
  }
  .fine-print {
    position: absolute;
    left: 34px;
    top: 640px;
    width: 1020px;
    color: var(--paper);
    font-weight: 700;
    font-size: 30px;
    line-height: 43px;
    letter-spacing: 0.6px;
    word-spacing: 4px;
  }
</style>
</head>
<body>
<main class="canvas">
  <section class="sign">
    <div class="title-plate"><h1>SURVEILLANCE</h1></div>
    <div class="notice-band">
      <div class="camera-illustration" role="img" aria-label="Line drawing of a wall-mounted bullet CCTV security camera with infrared LED ring"></div>
      <p class="notice-text">THIS<br>PROPERTY IS<br>PROTECTED<br>BY CCTV<br>SECURITY<br>CAMERAS</p>
    </div>
    <p class="fine-print">FOR YOUR PERSONAL PROTECTION ALL ACTIVITIES ARE<br>RECORDED ON DIGITAL MEDIA TO AID IN THE PROSECUTION<br>OF ANY CRIME COMMITTED ON THIS PROPERTY</p>
  </section>
</main>
</body>
</html>
```